Corporate Christmas Hamper Guide 2021

We are an online Hamper business in Australia and we need to design and produce our Christmas Hamper brochure for this year. It will need to be a pdf format which will become a digital online brochure. Our business Willowbay Baskets (www.willowbaybaskets.com.au) is a website that curates, packages and delivers hampers for both consumers and corporates. This specific brochure is targetted to the business market. The person who will review the brochure will generally be Executive assistants, Personal Assistants, Marketing Directors and their staff, Senior Managers as well as small business owners. Primaily they will be women.

Hampers are a luxury gift and Christmas is a traditional time for businesses to give their staff, clients, special customers and suppliers a gift to say thankyou for their support over the year. With Covid, this year has made it more difficult to stay connected to colleagues and clients and a hamper is a great way to do that so we anticipate it will be very popular this year.

I have attached our brochure from last year which was a super quick job (not done by a designer). We had recently purchased the business and we just needed to get something out. This is very substandard but I send it to you to see the sorts of things we will include in the brochure.

This job entails intial design and layout then once agreed final production including free image sourcing (hamper photography will be provided but other stylistic and suitable lifestyle photography to enhance the brochure will need to be sourced by you....royalty free). a more detailed design brief is attached below.

```html
<!DOCTYPE html>
<html lang="en">
<head>
<meta charset="utf-8">
<title>Willowbay Baskets – Corporate Gifting Guide 2021</title>
<link rel="stylesheet" href="https://fonts.googleapis.com/css2?family=Montserrat:wght@400;600;700;800&family=Playfair+Display:wght@700;900&display=swap">
<style>
:root{
  --ink:#222;
  --dark:#2b2c32;
  --dark-2:#1f2025;
  --red:#e4261c;
  --orange:#ff8a00;
  --white:#fff;
  --blush:#fbefea;
  --sand:#f6ebe1;
  --mist:#ececec;
  --paper:#f3f3f3;
}
*{box-sizing:border-box;margin:0;padding:0}
html,body{width:1200px;height:3439px;overflow:hidden}
body{position:relative;background:var(--white);font-family:"Montserrat",sans-serif;color:var(--ink)}
.abs{position:absolute}
.section{position:absolute;left:0;width:1200px;overflow:hidden}
.photo{position:absolute}
p{font-size:12px;line-height:19px}

/* hero */
.hero{top:0;height:674px;background:radial-gradient(ellipse at 30% 40%,#f4f4f4 0%,#dcdcdc 60%,#bdbdbd 100%)}
.hero .photo{left:507px;top:0;width:693px;height:674px;background:linear-gradient(160deg,#d8d8d8 0%,#c9231d 30%,#c77a3a 55%,#4b4b4d 80%,#d08c50 100%)}
.brand-name{left:110px;top:262px;width:340px;text-align:center;font-family:"Playfair Display",serif;font-weight:900;font-size:46px;line-height:46px;color:#2a2a2a}
.guide-title{left:100px;top:382px;width:360px;text-align:center;font-family:"Playfair Display",serif;font-weight:700;font-size:36px;line-height:42px;color:#1e1e1e}
.contact{left:63px;top:630px;font-size:13px;color:#444}
.contact span{margin:0 10px;color:#888}

/* intro */
.intro{top:688px;height:676px;background:linear-gradient(180deg,var(--dark) 0%,var(--dark-2) 100%)}
.dot{position:absolute;border-radius:50%;background:#9a9ba0;opacity:.8}
.watermark{font-family:"Playfair Display",serif;font-weight:900;font-size:160px;line-height:150px;color:rgba(255,255,255,.05);white-space:nowrap}
.intro-copy{left:167px;top:153px;width:520px;color:#fff;font-size:12.3px;line-height:23.6px}
.offer{left:812px;top:97px;width:307px;height:288px;background:var(--orange);color:#fff;padding:48px 24px 0}
.offer h3{font-size:12.5px;font-weight:700;margin-bottom:6px}
.offer p{font-size:12.3px;line-height:23.6px;text-align:justify}
.offer .note{font-style:italic;margin-top:24px}

/* tag labels */
.tag{position:absolute;background:var(--red);color:#fff;font-weight:700;font-size:24px;display:flex;align-items:center;justify-content:center}

/* product copy */
.item h4{display:flex;justify-content:space-between;font-size:12.5px;font-weight:700;margin-bottom:14px}
.item p{font-size:12px;line-height:19px}

.under100{top:1388px;height:398px;background:var(--blush)}
.under100 .right-panel{position:absolute;left:598px;top:0;width:602px;height:398px;background:var(--sand)}
.under100 .photo-a{left:0;top:30px;width:434px;height:368px;background:linear-gradient(150deg,#fdfdfd 20%,#e9c8a6 60%,#c4572c 100%)}
.under100 .photo-b{left:598px;top:100px;width:294px;height:270px;background:linear-gradient(150deg,#e9e6de 10%,#d9c34a 40%,#3b3b3b 70%,#c52822 100%)}

.wine{top:1786px;height:277px;background:var(--mist)}
.wine .photo{left:675px;top:24px;width:354px;height:242px;background:linear-gradient(150deg,#2a2a2a 30%,#d7261e 70%,#e8e8e8 100%)}
.wine-copy{left:77px;top:60px;width:500px}
.wine-copy h4{font-size:12.5px;font-weight:700;margin-bottom:16px}
.choices{display:grid;grid-template-columns:258px 240px;font-size:12.3px;line-height:19px;margin-bottom:10px}

.under160{top:2083px;height:674px;background:linear-gradient(180deg,#2c2d33,#25262b)}
.under160 .photo-c{left:263px;top:138px;width:299px;height:452px;background:linear-gradient(170deg,#bdbdbd 0%,#f2f2f2 35%,#d8a33a 65%,#6c2d2d 100%)}
.under160 .photo-d{left:577px;top:138px;width:307px;height:219px;background:linear-gradient(160deg,#f4f4f4 30%,#6a3a8a 60%,#2c3a5a 100%)}
.under160 .photo-e{left:577px;top:371px;width:307px;height:219px;background:linear-gradient(150deg,#e9e6de 10%,#d9c34a 40%,#3b3b3b 70%,#c52822 100%)}
.under160 .item{color:#fff}
.under160 .item h4{font-size:11px;margin-bottom:4px;display:block}
.under160 .item p{font-size:10.6px;line-height:19px}
.after-work{left:27px;top:366px;width:214px;text-align:right}
.sweet{left:902px;top:144px;width:268px}
.green{left:906px;top:421px;width:270px}

.deluxe{top:2757px;height:682px;background:var(--paper)}
.deluxe .photo{left:427px;top:126px;width:761px;height:535px;background:linear-gradient(160deg,#f3f3f3 0%,#e0642a 30%,#1f2a44 55%,#d8b23a 80%,#c92a22 100%)}
.best{left:45px;top:278px;width:350px}
.best h4{font-size:11.5px;margin-bottom:20px}
.best p{font-size:11.3px;line-height:18.8px}
</style>
</head>
<body>

<section class="section hero">
  <div class="photo" role="img" aria-label="Stacked wrapped Christmas gifts with red ribbon, baubles and a grey and orange magnetic gift box on a soft snowy background"></div>
  <div class="abs brand-name">Willowbay<br>Baskets</div>
  <h1 class="abs guide-title">Corporate Gifting<br>Guide 2021</h1>
  <div class="abs contact">1300 41 62 80<span>|</span>www.willowbaybaskets.com.au<span>|</span>corporate@willowbaybaskets.com.au</div>
</section>

<section class="section intro">
  <span class="dot" style="left:210px;top:102px;width:30px;height:30px"></span>
  <span class="dot" style="left:105px;top:300px;width:30px;height:30px"></span>
  <span class="dot" style="left:228px;top:407px;width:30px;height:30px"></span>
  <span class="dot" style="left:49px;top:400px;width:9px;height:9px"></span>
  <span class="dot" style="left:343px;top:441px;width:6px;height:6px"></span>
  <div class="abs watermark" style="left:545px;top:440px">Willowbay</div>
  <div class="abs watermark" style="left:350px;top:560px">Baskets</div>
  <p class="abs intro-copy">Show your clients how much you appreciate them this Christmas! And what better way to express your gratitude than by sending them a beautiful handpacked hamper from the team at Willowbay Baskets. We will deliver your corporate gifts anywhere around Australia with FREE Standard Shipping. Or for an additional cost of just $9.95 per hamper there is the Premium service of 1 - 2 Business Day delivery. Why not tailor your gifts with a free gift card and customised ribbon with your business logo, for maximum brand impact. Quality assured, handpicked and taste-tested by our friends, family and staff; the artisan, luxury and award-winning brands we house here at Willowbay Baskets are a genuine pleasure to share.</p>
  <aside class="abs offer">
    <h3>Early Bird Special</h3>
    <p>Receive 5% OFF when you order 10 or more hampers and pay by 13 November. Simply complete our Bulk Order Form and email to corporate@willowbaybaskets.com.au and we will apply the discount to your final invoice.</p>
    <p class="note">*Discount does not apply to shipping*</p>
  </aside>
</section>

<section class="section under100">
  <div class="right-panel"></div>
  <div class="photo photo-a" role="img" aria-label="White gift box filled with snacks, chocolate coconut rolls and a copper ribbon"></div>
  <div class="photo photo-b" role="img" aria-label="Snack hamper with tortilla chips, popcorn, nuts and chocolate bites in a white tray with red ribbon"></div>
  <div class="tag" style="left:494px;top:3px;width:200px;height:55px">UNDER $100</div>
  <div class="abs item" style="left:323px;top:103px;width:237px">
    <h4><span>TemptingTreats</span><span>$75</span></h4>
    <p>Here’s a bit of all things tempting! This corporate best seller is packed full of goodies for its lucky recipients. Includes our mouth-watering Pretzels, Beer Nuts, Shortbread Bites, Crackerthins, Soft Jubes, Choc fruit and nuts and Crispy Chocolate Coconut Rolls.</p>
  </div>
  <div class="abs item" style="left:907px;top:103px;width:260px">
    <h4><span>FeelingPeckish</span><span>$89</span></h4>
    <p>Snack Attack? A great share pack for the whole team. Chock full of tasty sweet and savoury treats including Sol Dorado Chipotle and Lime Tortilla Chips, Salted Pretzels, Caramel Covered Popcorn, Hattie's Handmade Double Choc Chip Bites, Handmade Chocolate Roadblock, Beer Nuts and Soft Jubes</p>
  </div>
</section>

<section class="section wine">
  <div class="photo" role="img" aria-label="Black leather-look wine case holding a white wine bottle and accessories, tied with red ribbon"></div>
  <div class="abs wine-copy">
    <h4>LuxuryWineCase &amp; Wine of Choice $35 +wine</h4>
    <div class="choices">
      <span>Choose from</span><span>Kestrel Ridge Rosé +$30</span>
      <span>Harbour Lane Sauvignon Blanc +$25</span><span>Banksia Hill Cabernet Merlot +$40</span>
      <span>Tallowood Pinot Noir +$25</span><span>Stonecrest Shiraz +$65</span>
    </div>
    <p>A simple yet sophisticated corporate gift. Choose from 5 different wines, presented in a mock-leather wine case which includes a bottle opener/corkscrew, a pouring spout, drip-stop ring and foil cutter</p>
  </div>
</section>

<section class="section under160">
  <div class="tag" style="left:494px;top:2px;width:200px;height:71px">UNDER $160</div>
  <div class="photo photo-c" role="img" aria-label="After work drinks hamper with red wine, tortilla chips, almonds, fudge and crackers"></div>
  <div class="photo photo-d" role="img" aria-label="Christmas chocolates hamper with bon bons, caramel sauce and an orange bow"></div>
  <div class="photo photo-e" role="img" aria-label="Garden self care hamper with hand cream, hand wash, citronella candle and towel"></div>
  <div class="abs item after-work">
    <h4>AfterWorkDrinks $129</h4>
    <p>Ready, Set, Go! Everything needed for a Team gathering after work. Say thank you and celebrate what has been a tough year for so many. A gesture at Christmas shows you care. Includes Redgum Flat Shiraz, Chipotle and Lime Tortilla Chips, Salted Cashews, Milk Chocolate Scorched Almonds, Crunchy Brittle, Hattie's handmade Choc Chip Bites, Crackers, mini Raspberry Meringues and Choc Mint Fudge.</p>
  </div>
  <div class="abs item sweet">
    <h4>SweetChristmasBites $119</h4>
    <p>Enjoy the tasty treats on offer with this gourmet gift hamper! Includes our selection of Chocolates from Ashford Lane &amp; Rosa &amp; Reed, Salted Caramel Sauce, a touch of Festive Fare with our Gingerbread Christmas Cookie, White Choc Christmas slice, Christmas Freckle and some sparkly additions for him and her from Lumen Jewels Sparkle Crystal Christmas Bon Bon's! (Contains 2 Bon Bons containing one set of; Necklace, Earrings, Tie Clip or Cufflinks)</p>
  </div>
  <div class="abs item green">
    <h4>GreenThumb $109</h4>
    <p>Our best selling staff favourite is all about self care while enjoying the beautiful outdoors. Botanically inspired and designed for hardworking Gardeners. Includes Fernleaf Botanics nourishing Wild Lime &amp; Mint SPF 15+ UVA and UVB protection hand cream, their gentle Therapy Garden Hand Wash, natural scented Citronella Candle and Hand Towel</p>
  </div>
</section>

<section class="section deluxe">
  <div class="tag" style="left:0;top:31px;width:200px;height:76px">DELUXE</div>
  <div class="photo" role="img" aria-label="Luxury hamper spread with champagne, wine, glasses, chocolates, games, snacks and a wine cooler"></div>
  <div class="abs item best">
    <h4><span>TheBest of Everything</span><span>$869</span></h4>
    <p>What a selection! We have put together the ultimate in gift giving, so you can say “Thank You” in a way that words can’t. From the finest French Champagne to luxury Australian Chocolates and treats, to games and Premier Lounge Movie Tickets. It’s a real statement of thanks for a job well done! Includes: Carrick &amp; Co Chocolate Box, Sol Dorado Lime &amp; Chipotle Corn Chips, Rosa &amp; Reed Chocolate Cranberries, Pretzels and Coffee Beans, Ashford Lane’s Choc Macadamias, Choc Berries, Scorched Almonds and Fruit &amp; Nut, Langues De Chat Raspberry Biscuits, Lavosh Fennel &amp; Thyme Biscuits, Hattie's Savoury Parmesan &amp; Paprika Bites, Choc Fudge Cookie Bites, Ember Roasters Espresso Blend, Coral Bay Wine Platter Pack, Salted Cashews, Truffle Oil &amp; Salts Pack, Salted Caramel Fudge, Quince Paste, Vallon Cheese Knives, Mallee Creek McLaren Vale Shiraz, Maison Clairval, Wine Cooler Bucket, Parlour Games Compendium and 2 Premier Lounge Movie Tickets.</p>
  </div>
</section>

</body>
</html>
```